Capability statement for an Electrical Business based in Sydney Australia

The aim for the Capability statement is for us to look more professional when we meet someone or after cold calling and have to send them our business details.
Need something simple, efficient and to the point.

It should have the following content
- Our mission (details can be as attached PDF)
- Areas we service (this can be a google map of areas we service but basically the areas are
Metro Sydney with our work centralised around the Norwest, Hills, Inner west and Epping area)
- List of services we provide (as PDF)
- Details about us; who we are, contact details, licenses (as PDF)
- Why they should choose us
(As pdf)

Right now, we're just after a nice format we're happy with, the details we are happy to provide with once we have a design in mind.

I've attached our current existing capability statement and what our details are. Also, our website is
https://themardenfield.com.au/

Thanks in advance!

• Should not be complicated for the reader

```html
<!DOCTYPE html>
<html lang="en">
<head>
<meta charset="utf-8">
<title>The Marden Field – Capability Statement</title>
<link href="https://fonts.googleapis.com/css2?family=Michroma&family=Poppins:wght@400;500;600;700;800&display=swap" rel="stylesheet">
<style>
  :root {
    --red: #e0352b;
    --red-dark: #b9241c;
    --black: #0d0d0d;
    --white: #ffffff;
    --ink: #1a1a1a;
    --grey: #d9d9d9;
    --line: #cfcfcf;
    --text-light: #f2f2f2;
  }
  * { box-sizing: border-box; margin: 0; padding: 0; }
  html, body { width: 834px; height: 1200px; overflow: hidden; background: #e4e4e4; }
  .canvas { position: relative; width: 834px; height: 1200px; }

  .frame { position: absolute; left: 192px; width: 450px; height: 582px; overflow: hidden; box-shadow: 0 6px 16px rgba(0,0,0,.28); }
  .frame-capability { top: 12px; }
  .frame-why { top: 606px; }
  .page {
    position: absolute; left: 0; top: 0; width: 643px; height: 832px;
    transform: scale(0.7); transform-origin: 0 0;
    background: var(--white); font-family: "Poppins", sans-serif; color: var(--ink);
  }
  .abs { position: absolute; }

  /* brand */
  .brand { left: 36px; top: 44px; display: flex; align-items: center; gap: 8px; }
  .brand-dot { width: 13px; height: 13px; border-radius: 50%; background: var(--red); }
  .brand-name { font-family: "Michroma", sans-serif; font-size: 19px; color: var(--red); letter-spacing: 1px; line-height: 1.2; }

  .rule { left: 37px; width: 291px; height: 2px; background: var(--red); }
  .rule::before { content: ""; position: absolute; left: 0; top: -1px; width: 78px; height: 4px; background: var(--red); }

  /* capability page */
  .eyebrow { left: 37px; top: 118px; font-family: "Michroma", sans-serif; font-size: 17px; }
  .headline { left: 35px; top: 138px; font-family: "Michroma", sans-serif; font-size: 31px; line-height: 37px; font-weight: 400; }
  .headline .red { color: var(--red); display: block; }
  .headline .dark { color: var(--black); display: block; }
  .tagline { left: 37px; top: 228px; font-size: 16px; font-weight: 600; line-height: 20px; }
  .doc-title { left: 37px; top: 282px; font-size: 24px; font-weight: 700; color: var(--red); }
  .doc-title span { color: var(--black); }
  .mission { left: 35px; top: 324px; width: 300px; height: 92px; background: var(--black); padding: 12px 12px; color: var(--text-light); }
  .mission h2 { font-size: 16px; font-weight: 700; color: var(--red); margin-bottom: 6px; }
  .mission p { font-size: 9.6px; line-height: 12.5px; }
  .about-title { left: 36px; top: 430px; font-size: 16px; font-weight: 700; }
  .about-title span, .services-title span { color: var(--red); }
  .about-text { left: 36px; top: 456px; width: 222px; font-size: 9.4px; line-height: 12.6px; color: #222; }
  .bulbs { left: 264px; top: 418px; width: 72px; height: 184px; background: linear-gradient(180deg, #ffffff 0%, #f3e7cf 55%, #d9b57a 85%, #ffffff 100%); border-radius: 0 0 30px 30px; }

  .panel-capability { left: 344px; top: 0; width: 299px; height: 630px; }
  .services-title { left: 362px; top: 318px; font-size: 16px; font-weight: 700; color: var(--white); }
  .services { left: 362px; top: 346px; width: 270px; list-style: none; color: var(--text-light); font-size: 10.4px; line-height: 12.8px; }
  .services li { position: relative; padding-left: 15px; margin-bottom: 4px; }
  .services li::before { content: ""; position: absolute; left: 1px; top: 3px; width: 7px; height: 7px; border-radius: 50%; background: var(--red); box-shadow: inset 0 0 0 1.5px var(--red), inset 0 0 0 2.5px #fff; }

  .values-band { left: 0; top: 630px; width: 643px; height: 202px; }
  .values-tab { left: 200px; top: 628px; width: 240px; text-align: center; font-size: 21px; line-height: 32px; color: var(--black); font-weight: 500; }
  .values-tab b { color: var(--red); font-weight: 700; }
  .value-label { top: 724px; width: 70px; text-align: center; font-size: 8.6px; line-height: 10px; color: var(--white); }

  /* why page */
  .why-title { left: 35px; top: 112px; font-family: "Michroma", sans-serif; font-size: 37px; line-height: 42px; }
  .why-title .red { color: var(--red); display: block; }
  .why-title .dark { color: var(--black); display: block; }
  .why-sub { left: 37px; top: 202px; font-size: 20px; font-weight: 700; color: var(--red); }
  .reason { width: 280px; }
  .reason-head { display: flex; gap: 10px; align-items: flex-start; }
  .reason-icon { flex: none; width: 28px; height: 28px; border-radius: 4px; background: var(--red); display: flex; align-items: center; justify-content: center; }
  .reason h3 { font-size: 13.5px; font-weight: 700; line-height: 16.5px; }
  .reason p { margin-top: 14px; font-size: 9.4px; line-height: 12.4px; color: #222; }
  .reason-dark h3 { color: var(--white); }
  .reason-dark p { color: var(--text-light); margin-top: 12px; }
  .divider { height: 1px; background: var(--line); }
  .divider-dark { background: #555; }

  .panel-why { left: 343px; top: 0; width: 300px; height: 632px; background: var(--black); border-bottom-left-radius: 78px; overflow: hidden; }

  .contact-title { left: 36px; top: 650px; font-family: "Michroma", sans-serif; font-size: 25px; font-weight: 400; color: var(--black); -webkit-text-stroke: 0.6px var(--black); }
  .contact-title span { color: var(--red); -webkit-text-stroke: 0.6px var(--red); }
  .contact-row { display: flex; height: 20px; font-size: 12px; font-weight: 700; line-height: 20px; }
  .contact-row .who { width: 58px; background: var(--red); color: var(--white); padding-left: 10px; }
  .contact-row .num { width: 100px; background: var(--black); color: var(--white); padding-left: 6px; letter-spacing: .3px; }
  .contact-row .lic { width: 84px; }
  .web-line { font-size: 12px; font-weight: 600; display: flex; align-items: center; gap: 5px; color: var(--black); }
  .footer { left: 0; top: 755px; width: 643px; height: 77px; background: var(--black); }
  .liability { left: 37px; top: 771px; font-size: 21px; font-weight: 700; color: var(--white); }
  .liability span { color: var(--red); margin-left: 10px; }
  .abn { left: 395px; top: 770px; display: flex; height: 25px; font-size: 14px; font-weight: 700; line-height: 25px; letter-spacing: 2px; }
  .abn .tag { background: var(--red); color: var(--white); padding: 0 6px 0 10px; }
  .abn .val { background: var(--white); color: var(--black); padding: 0 6px; border: 2px solid var(--red); line-height: 21px; }
</style>
</head>
<body>
<main class="canvas">

  <!-- Capability statement page -->
  <div class="frame frame-capability">
    <section class="page page-capability">
      <div class="abs brand"><span class="brand-dot"></span><span class="brand-name">THE MARDEN FIELD</span></div>
      <p class="abs eyebrow">SYDNEY-BASED</p>
      <h1 class="abs headline"><span class="red">ELECTRICAL</span><span class="dark">BUSINESS</span></h1>
      <div class="abs rule" style="top:216px;"></div>
      <p class="abs tagline">Specialising in electrical<br>maintenance</p>
      <p class="abs doc-title">Capability <span>statement</span></p>

      <div class="abs mission">
        <h2>MISSION</h2>
        <p>Dedicate ourselves to providing world class service to anyone in need, based on honesty, communication and respect.</p>
      </div>

      <h2 class="abs about-title">WHO <span>WE ARE</span></h2>
      <p class="abs about-text">The Marden Field is a growing Electrical maintenance company based in the Inner West. We are established on sound service principles with honesty, communication, and respect at the forefront of every team member. We strive for openness, trust, and accountability and we are in the business of providing solutions to help others. We see ourselves as an extension of your team.</p>
      <div class="abs bulbs" role="img" aria-label="Hanging vintage filament light bulbs"></div>

      <svg class="abs panel-capability" viewBox="0 0 299 630">
        <rect width="299" height="630" fill="var(--black)"/>
        <path d="M0 0 H299 V225 C299 275 262 305 212 305 H87 C37 305 0 275 0 225 Z" fill="var(--red)"/>
        <foreignObject x="34" y="0" width="232" height="286">
          <div xmlns="http://www.w3.org/1999/xhtml" role="img" aria-label="Bright modern kitchen with white island, black bar stools and pendant lights" style="width:232px;height:286px;border-radius:0 0 72px 72px;background:linear-gradient(180deg,#f4f2ee 0%,#e3ded6 45%,#bfb4a6 75%,#4a3a2e 100%);"></div>
        </foreignObject>
        <rect x="106" y="0" width="60" height="40" fill="var(--red)"/>
      </svg>

      <h2 class="abs services-title">WHO <span>WE ARE</span></h2>
      <ul class="abs services">
        <li>24/7 Emergency service</li>
        <li>Switchboard UPGRADE and REPAIRS</li>
        <li>Light fitting installations</li>
        <li>Powerpoint installations</li>
        <li>Surge device installations</li>
        <li>Testing and servicing electric hot<br>water systems</li>
        <li>Smoke Alarm installation with<br>compliance certificate</li>
        <li>Electric Vehicle charging stations</li>
        <li>Ceiling and Exhaust fan installations<br>with roof and wall venting</li>
        <li>Appliance installations</li>
        <li>Fault finding</li>
        <li>TV, DATA and FREE TO AIR Aerial<br>installations</li>
      </ul>

      <svg class="abs values-band" viewBox="0 0 643 202">
        <defs>
          <linearGradient id="bandShade" x1="0" y1="0" x2="0" y2="1">
            <stop offset="0" stop-color="var(--red)"/>
            <stop offset="1" stop-color="var(--red-dark)"/>
          </linearGradient>
        </defs>
        <rect width="643" height="194" fill="url(#bandShade)"/>
        <rect y="194" width="643" height="8" fill="var(--black)"/>
        <path d="M200 0 H440 L420 30 H220 Z" fill="var(--grey)"/>
        <g fill="none" stroke="#fff" stroke-width="2">
          <path d="M150 105 H190"/><path d="M185 100 L190 105 L185 110"/>
          <path d="M296 105 H336"/><path d="M331 100 L336 105 L331 110"/>
          <path d="M443 105 H483"/><path d="M478 100 L483 105 L478 110"/>
        </g>
        <g id="ring1">
          <circle cx="98" cy="105" r="57" fill="var(--black)"/>
          <circle cx="98" cy="105" r="50" fill="none" stroke="#fff" stroke-width="2.5" stroke-dasharray="250 65" transform="rotate(-40 98 105)"/>
          <circle cx="98" cy="105" r="40" fill="var(--black)" stroke="var(--red)" stroke-width="2.5"/>
          <path d="M98 74 l9 4 v6 c0 6 -4 10 -9 12 c-5 -2 -9 -6 -9 -12 v-6 z" fill="#fff"/>
          <path d="M94 84 l3 3 l6 -6" stroke="var(--black)" stroke-width="2" fill="none"/>
        </g>
        <g>
          <circle cx="243" cy="105" r="57" fill="var(--black)"/>
          <circle cx="243" cy="105" r="50" fill="none" stroke="#fff" stroke-width="2.5" stroke-dasharray="250 65" transform="rotate(-40 243 105)"/>
          <circle cx="243" cy="105" r="40" fill="var(--black)" stroke="var(--red)" stroke-width="2.5"/>
          <path d="M235 91 l6 -14 h11 l-3 8 h6 l-11 15 h-9 z" fill="#fff"/>
        </g>
        <g>
          <circle cx="389" cy="105" r="57" fill="var(--black)"/>
          <circle cx="389" cy="105" r="50" fill="none" stroke="#fff" stroke-width="2.5" stroke-dasharray="250 65" transform="rotate(-40 389 105)"/>
          <circle cx="389" cy="105" r="40" fill="var(--black)" stroke="var(--red)" stroke-width="2.5"/>
          <circle cx="389" cy="86" r="8" fill="none" stroke="#fff" stroke-width="4" stroke-dasharray="3 2.5"/>
          <circle cx="389" cy="86" r="3" fill="#fff"/>
        </g>
        <g>
          <circle cx="537" cy="105" r="57" fill="var(--black)"/>
          <circle cx="537" cy="105" r="50" fill="none" stroke="#fff" stroke-width="2.5" stroke-dasharray="250 65" transform="rotate(-40 537 105)"/>
          <circle cx="537" cy="105" r="40" fill="var(--black)" stroke="var(--red)" stroke-width="2.5"/>
          <path d="M537 76 l3 6 l6.5 1 l-4.5 4.5 l1 6.5 l-6 -3 l-6 3 l1 -6.5 l-4.5 -4.5 l6.5 -1 z" fill="#fff"/>
        </g>
      </svg>
      <p class="abs values-tab"><b>CORE</b> VALUES</p>
      <p class="abs value-label" style="left:63px;">Safety and<br>Security is<br>priority</p>
      <p class="abs value-label" style="left:208px;">Support<br>when you<br>need it<br>most</p>
      <p class="abs value-label" style="left:354px;">Service with<br>an over<br>the-top<br>WOW</p>
      <p class="abs value-label" style="left:502px;">Satisfaction<br>with loyalty<br>and<br>integrity</p>
    </section>
  </div>

  <!-- Why choose page -->
  <div class="frame frame-why">
    <section class="page page-why">
      <div class="abs brand"><span class="brand-dot"></span><span class="brand-name">THE MARDEN FIELD</span></div>
      <h1 class="abs why-title"><span class="red">WHY</span><span class="dark">CHOOSE</span></h1>
      <p class="abs why-sub">THE MARDEN FIELD</p>
      <div class="abs rule" style="top:243px;"></div>

      <div class="abs reason" style="left:37px;top:272px;">
        <div class="reason-head">
          <span class="reason-icon"><svg width="16" height="16" viewBox="0 0 16 16"><path d="M3 10 l5 -8 l5 8 z M5 12 h6 v2 h-6 z" fill="#fff"/></svg></span>
          <h3>Support when you<br>need it most</h3>
        </div>
        <p>The Marden Field provides around the clock assistance, whether during normal business hours or emergencies we are focused on providing solutions for our clients.</p>
      </div>
      <div class="abs divider" style="left:37px;top:382px;width:275px;"></div>

      <div class="abs reason" style="left:37px;top:396px;">
        <div class="reason-head">
          <span class="reason-icon"><svg width="16" height="16" viewBox="0 0 16 16"><circle cx="8" cy="8" r="5" fill="none" stroke="#fff" stroke-width="3" stroke-dasharray="2.5 1.5"/><circle cx="8" cy="8" r="2" fill="#fff"/></svg></span>
          <h3>Fast and responsive team<br>with a direct contact</h3>
        </div>
        <p>The Marden Field treats every one of our clients as a VIP. We pride ourselves on being able to provide a quick turn around for all our jobs. We make the whole process smooth, from booking the job to attending and completion.</p>
      </div>
      <div class="abs divider" style="left:37px;top:522px;width:275px;"></div>

      <div class="abs reason" style="left:37px;top:538px;">
        <div class="reason-head">
          <span class="reason-icon"><svg width="16" height="16" viewBox="0 0 16 16"><path d="M8 1 l2 4 l4.5 .6 l-3.2 3.1 l.8 4.5 l-4.1 -2.2 l-4.1 2.2 l.8 -4.5 l-3.2 -3.1 l4.5 -.6 z" fill="#fff"/></svg></span>
          <h3>Satisfaction with loyalty<br>and integrity</h3>
        </div>
        <p>We value our transparency and communication skills to deliver an outstanding performance which reflects our happy customer base.</p>
      </div>

      <div class="abs panel-why">
        <svg width="300" height="632" viewBox="0 0 300 632" style="position:absolute;left:0;top:0;">
          <path d="M0 0 H300 V262 C300 312 265 342 215 342 H85 C35 342 0 312 0 262 Z" fill="var(--red)"/>
          <rect x="0" y="0" width="120" height="75" fill="var(--red-dark)" opacity="0"/>
          <foreignObject x="35" y="75" width="234" height="262">
            <div xmlns="http://www.w3.org/1999/xhtml" role="img" aria-label="Warm-lit kitchen at night with wooden cabinets, island bench and glass pendant lights" style="width:234px;height:262px;border-radius:0 0 70px 70px;background:linear-gradient(180deg,#3a2418 0%,#6b4630 40%,#a98468 70%,#2b1c14 100%);"></div>
          </foreignObject>
        </svg>
        <div class="abs reason reason-dark" style="left:27px;top:375px;width:250px;">
          <div class="reason-head">
            <span class="reason-icon"><svg width="16" height="16" viewBox="0 0 16 16"><circle cx="8" cy="5.5" r="3" fill="#fff"/><path d="M2.5 14 c0 -4 2.5 -5.5 5.5 -5.5 s5.5 1.5 5.5 5.5 z" fill="#fff"/></svg></span>
            <h3>We provide<br>courtesy calls</h3>
          </div>
          <p>The appointment will be confirmed the day before and our technicians will call you half an hour in advance on approach to the job</p>
        </div>
        <div class="abs divider divider-dark" style="left:17px;top:480px;width:263px;"></div>
        <div class="abs reason reason-dark" style="left:27px;top:505px;width:250px;">
          <div class="reason-head">
            <span class="reason-icon"><svg width="16" height="16" viewBox="0 0 16 16"><path d="M3 1 h8 l2 2 v12 h-10 z" fill="#fff"/><path d="M5 6 h6 M5 9 h4" stroke="var(--red)" stroke-width="1.3"/></svg></span>
            <h3>Licensed and insured<br>technicians</h3>
          </div>
          <p>All our technicians are experts of their field, with the relevant equipment, knowledge and licenses to carry out our duties.</p>
        </div>
      </div>

      <h2 class="abs contact-title">CONTACT <span>US</span></h2>
      <div class="abs contact-row" style="left:37px;top:692px;"><span class="who">Liam</span><span class="num">0412 555 018</span></div>
      <div class="abs contact-row" style="left:37px;top:718px;"><span class="who">Owen</span><span class="num">0433 555 027</span></div>
      <p class="abs web-line" style="left:210px;top:693px;">
        <svg width="12" height="10" viewBox="0 0 12 10"><rect width="12" height="10" rx="1" fill="var(--red)"/><path d="M1 1.5 L6 5.5 L11 1.5" stroke="#fff" stroke-width="1.2" fill="none"/></svg>
        services@themardenfield.com.au</p>
      <p class="abs web-line" style="left:210px;top:719px;">
        <svg width="11" height="11" viewBox="0 0 12 12"><circle cx="6" cy="6" r="5.5" fill="var(--red)"/><path d="M0.5 6 H11.5 M6 0.5 C3 3.5 3 8.5 6 11.5 M6 0.5 C9 3.5 9 8.5 6 11.5" stroke="#fff" stroke-width=".9" fill="none"/></svg>
        www.themardenfield.com.au</p>
      <div class="abs contact-row" style="left:462px;top:691px;"><span class="who">Liam</span><span class="num lic">500112C</span></div>
      <div class="abs contact-row" style="left:462px;top:718px;"><span class="who">Owen</span><span class="num lic">41207C</span></div>

      <div class="abs footer"></div>
      <p class="abs liability">Public Liability<span>$20,000,000</span></p>
      <p class="abs abn"><span class="tag">ABN</span><span class="val">5102 4488 316</span></p>
    </section>
  </div>

</main>
</body>
</html>
```